Business Card

Creative young company is looking for a innovation businesscard

We are a IT company wich provide as core business VoIP, Hosting, Server, and we also sell internet lines.

The businesscard must be modern and it must match with our company, think of a IT (cloud) theme.

Company name :
OLMO IT

Adress :
Pelikaanstraat 27B
4917 KR Zwolle

www.olmo-it.nl
t.brink@olmo-it.nl

My name:
Tobias Brink

```html
<!DOCTYPE html>
<html lang="en">
<head>
<meta charset="utf-8">
<title>OLMO IT – Business Card</title>
<link rel="stylesheet" href="https://fonts.googleapis.com/css2?family=Exo+2:wght@400;500;600;800&display=swap">
<style>
  :root {
    --stage: #4b4c4b;
    --blue-light: #3a97e0;
    --blue-mid: #1f6fb8;
    --blue-dark: #0f3a68;
    --brand-blue: #1e6fb5;
    --ink: #3d3f42;
    --white: #ffffff;
    --paper: #f4f6f8;
    --line: #d6d9dd;
    --shadow: rgba(0, 0, 0, 0.35);
  }
  * { box-sizing: border-box; margin: 0; padding: 0; }
  html, body { width: 1200px; height: 780px; overflow: hidden; }
  body {
    background: var(--stage);
    font-family: "Exo 2", sans-serif;
    position: relative;
  }
  .card {
    position: absolute;
    width: 540px;
    height: 320px;
    overflow: hidden;
    box-shadow: 0 10px 24px var(--shadow);
  }

  /* Front */
  .card--front {
    left: 70px;
    top: 60px;
    background: radial-gradient(ellipse 70% 80% at 50% 55%, var(--blue-light) 0%, var(--blue-mid) 45%, var(--blue-dark) 100%);
  }
  .front-band {
    position: absolute;
    left: 0;
    top: 96px;
    width: 540px;
    height: 118px;
  }
  .front-brand {
    position: absolute;
    left: 0;
    right: 0;
    top: 112px;
    text-align: center;
  }
  .brand-name {
    font-weight: 800;
    color: var(--ink);
    letter-spacing: 2px;
    line-height: 1;
    display: inline-flex;
    align-items: center;
    gap: 14px;
  }
  .brand-dot {
    display: inline-block;
    border-radius: 50%;
    background: var(--brand-blue);
  }
  .front-brand .brand-name { font-size: 62px; }
  .front-brand .brand-dot { width: 34px; height: 34px; }
  .tagline {
    display: block;
    font-weight: 800;
    color: var(--brand-blue);
    letter-spacing: 1px;
  }
  .front-brand .tagline { font-size: 19px; margin-top: 4px; }

  /* Back */
  .card--back {
    left: 590px;
    top: 400px;
    background: var(--paper);
  }
  .back-photo {
    position: absolute;
    inset: 0;
    background:
      linear-gradient(180deg, rgba(255,255,255,0.9) 0%, rgba(240,240,240,0.6) 35%, rgba(205,195,185,0.55) 70%, rgba(235,235,235,0.85) 100%),
      linear-gradient(90deg, #e6e2dc 0%, #cfc6bb 40%, #d8d4cd 70%, #e9e7e4 100%);
  }
  .name-box {
    position: absolute;
    left: 0;
    top: 150px;
    width: 262px;
    height: 68px;
    background: linear-gradient(90deg, var(--blue-dark), var(--blue-mid));
    color: var(--white);
    text-align: center;
    padding-top: 8px;
  }
  .person-name { font-size: 27px; font-weight: 600; line-height: 1.1; }
  .person-role { font-size: 15px; font-weight: 500; }
  .contact-box {
    position: absolute;
    left: 262px;
    top: 96px;
    width: 278px;
    height: 122px;
  }
  .contact-shape { position: absolute; inset: 0; }
  .contact-list {
    position: absolute;
    right: 20px;
    top: 22px;
    list-style: none;
    text-align: right;
    color: var(--brand-blue);
    font-size: 14px;
    font-weight: 500;
    line-height: 20px;
  }
  .contact-list li { display: flex; justify-content: flex-end; align-items: center; gap: 6px; }
  .contact-list .address { align-items: flex-start; margin-top: 8px; }
  .contact-icon { width: 16px; height: 16px; flex: none; }
  .back-brand {
    position: absolute;
    left: 0;
    right: 0;
    top: 238px;
    text-align: center;
  }
  .back-brand .brand-name { font-size: 34px; gap: 8px; }
  .back-brand .brand-dot { width: 18px; height: 18px; }
  .back-brand .tagline { font-size: 11px; margin-top: 2px; }
</style>
</head>
<body>

<section class="card card--front">
  <svg class="front-band" viewBox="0 0 540 118" aria-hidden="true">
    <polygon points="0,10 158,10 172,0 186,10 540,10 540,118 0,118" fill="#ffffff"/>
  </svg>
  <div class="front-brand">
    <span class="brand-name"><span class="brand-dot"></span>OLMO IT</span>
    <span class="tagline">ALWAYS CONNECTED</span>
  </div>
</section>

<section class="card card--back">
  <div class="back-photo" role="img" aria-label="Faded photo of an office workspace with desks and monitors"></div>

  <div class="name-box">
    <div class="person-name">Tobias Brink</div>
    <div class="person-role">owner</div>
  </div>

  <div class="contact-box">
    <svg class="contact-shape" width="278" height="122" viewBox="0 0 278 122" aria-hidden="true">
      <polygon points="0,8 10,8 20,0 30,8 278,8 278,122 0,122" fill="#ffffff" stroke="#d6d9dd"/>
    </svg>
    <ul class="contact-list">
      <li>t.brink@olmo-it.nl
        <svg class="contact-icon" viewBox="0 0 16 16" aria-hidden="true"><rect x="1.5" y="3.5" width="13" height="9" fill="none" stroke="#1e6fb5" stroke-width="1.4"/><polyline points="1.5,3.5 8,9 14.5,3.5" fill="none" stroke="#1e6fb5" stroke-width="1.4"/></svg>
      </li>
      <li>www.olmo-it.nl
        <svg class="contact-icon" viewBox="0 0 16 16" aria-hidden="true"><g fill="none" stroke="#1e6fb5" stroke-width="1.3"><circle cx="8" cy="8" r="6.5"/><ellipse cx="8" cy="8" rx="2.8" ry="6.5"/><line x1="1.5" y1="8" x2="14.5" y2="8"/><line x1="2.5" y1="4.5" x2="13.5" y2="4.5"/><line x1="2.5" y1="11.5" x2="13.5" y2="11.5"/></g></svg>
      </li>
      <li class="address"><span>Pelikaanstraat 27B<br>4917 KR Zwolle</span>
        <svg class="contact-icon" viewBox="0 0 16 16" aria-hidden="true"><path d="M8 1a5 5 0 0 0-5 5c0 3.8 5 9 5 9s5-5.2 5-9a5 5 0 0 0-5-5z" fill="#1e6fb5"/><circle cx="8" cy="6" r="1.9" fill="#ffffff"/></svg>
      </li>
    </ul>
  </div>

  <div class="back-brand">
    <span class="brand-name"><span class="brand-dot"></span>OLMO IT</span>
    <span class="tagline">ALWAYS CONNECTED</span>
  </div>
</section>

</body>
</html>
```